Beautiful, sharp, website design for family-run property development company.

We are property developers in Kent (south east of London) who want to see the local town change. We are the only local property developer that is a family run business, focussing primarily on converting old, dilapidated Victorian buildings into beautiful residential spaces. Unlike other national developers, we work to regenerate buildings to create new employment opportunities, housing, and revive the town Centre .

Target Market(s)

1. Investors and Joint Venture partners - people with money to invest in property
2. Buyers of property - 25 to 40 year old, young professionals.
3. Commercial funders (people lending money to our projects
4. Professional team: Architects, builders, Estate agent who want to work with us

Industry/Entity Type

Real Estate Development

Coding

Number of Pages Required

Font styles to use
Other font styles liked:
• Please follow the brief of stylish, elegant, modern

Colors

Designer to choose colors to be used in the design.

Requirements
Must have
• Please use these websites as a reference of what we are looking to achieve.
• http://brellmoorhomes.com/#page5
• https://fernwick.co.uk/
• http://ambertide.co.uk/
• http://www.theharroweyestates.co.uk/about-harrowey
• Clean, simple, elegant, minimal design.
• Images of interiors of houses that have been converted from old buildings
• Images of farm buildings e.g. barns that have been converted to new homes or offices. Images of properties that may have been an old factory or old commercial property that is now a trendy apartment.
• Please use images of properties and interiors that are from the South East of England (including Kent, Surrey, Sussex, Hampshire, Dorset). There is a distinct style of housing in this part of England.
Nice to have
• Colours consistent with our brand colour palette (attached)

```html
<!DOCTYPE html>
<html lang="en">
<head>
<meta charset="utf-8">
<title>Larchfield Property – Home</title>
<link rel="stylesheet" href="https://fonts.googleapis.com/css2?family=Montserrat:wght@400;500;600&family=Lato:wght@400;700&display=swap">
<style>
:root{
  --teal:#7f9e97;
  --teal-light:#9bb3ad;
  --teal-dark:#6f8f88;
  --ink:#1d1d1f;
  --panel:#232325;
  --white:#ffffff;
  --muted:#d8d8d8;
  --line:rgba(255,255,255,.55);
}
*{box-sizing:border-box;margin:0;padding:0}
html,body{width:1200px;height:3590px;overflow:hidden}
body{background:var(--ink);color:var(--white);font-family:"Lato",sans-serif;position:relative}
.abs{position:absolute}
.heading{font-family:"Montserrat",sans-serif;font-weight:500;font-size:36px;line-height:1.12}
.heading span{color:var(--teal)}
.pill{display:flex;align-items:center;justify-content:center;gap:8px;border-radius:30px;background:var(--teal);color:var(--white);font:700 14px "Lato",sans-serif;text-transform:uppercase}
.pill svg{width:14px;height:14px}

/* hero */
.hero{left:0;top:0;width:1200px;height:600px}
.hero-left{left:0;top:0;width:600px;height:600px;background:linear-gradient(160deg,#5d5b56,#8a8780 45%,#6b6862)}
.hero-right{left:600px;top:0;width:600px;height:600px;background:linear-gradient(200deg,#d9d8d4,#b9b6ae 50%,#8f8670 80%,#b8953c)}
.brand{left:111px;top:76px;display:flex;align-items:center;gap:10px;font:500 19px "Montserrat",sans-serif;color:var(--teal-light);letter-spacing:.5px}
.brand i{width:12px;height:12px;border-radius:50%;background:var(--teal-light);display:block}
.nav{left:419px;top:51px;display:flex;gap:28px;font:700 14px "Lato",sans-serif;text-transform:uppercase}
.nav a{color:var(--white);text-decoration:none}
.nav a.active{color:var(--teal-light)}
.nav-rule{left:111px;top:119px;width:977px;height:1px;background:var(--line)}
.dots{left:572px;top:565px;display:flex;gap:4px}
.dots b{width:8px;height:8px;border-radius:50%;background:var(--white)}
.dots b.on{background:transparent;border:2px solid var(--white)}

/* about */
.about{left:0;top:600px;width:1200px;height:635px;background:var(--panel)}
.about-bg{left:811px;top:0;width:389px;height:596px;background:linear-gradient(160deg,#2b3b52,#1d2a3d 60%,#152031)}
.about-title{left:111px;top:135px}
.about-copy{left:111px;top:235px;width:462px;font-size:14px;line-height:32.5px;color:var(--white)}
.about-btn{left:111px;top:450px;width:156px;height:53px}
.about-photo{left:676px;top:150px;width:412px;height:354px;border:1px solid #9fb3ae;background:linear-gradient(180deg,#e9e6e1,#cfccc5 60%,#b7b3aa)}

/* services */
.services{left:0;top:1235px;width:1200px;height:514px;background:linear-gradient(180deg,#2a2a2c,#333236 50%,#3b3a3d)}
.services-title{left:0;top:68px;width:1200px;text-align:center}
.services-copy{left:195px;top:135px;width:810px;text-align:center;font-size:14px;line-height:36.5px}
.service{top:270px;width:160px;text-align:center}
.service svg{width:132px;height:132px;display:block;margin:0 auto}
.service p{margin-top:12px;font:700 14px "Lato",sans-serif;text-transform:uppercase}

/* projects */
.projects{left:0;top:1749px;width:1200px;height:774px;background:var(--ink)}
.projects-title{left:0;top:84px;width:1200px;text-align:center}
.tile{width:238px;height:232px}
.tile-hover{background:rgba(127,158,151,.93);display:flex;flex-direction:column;align-items:center;justify-content:center;text-align:center;padding:0 18px}
.tile-hover h3{font:700 14px "Lato",sans-serif;text-transform:uppercase;margin:12px 0 10px}
.tile-hover p{font-size:14px;line-height:25px}
.tile-hover a{color:var(--white);font-size:14px;margin-top:6px;display:flex;gap:6px;align-items:center}

/* cta */
.cta{left:0;top:2523px;width:1200px;height:188px;background:var(--teal)}
.cta-side{left:0;top:0;width:1200px;height:188px}
.cta-lead{left:110px;top:62px;font:500 20px "Montserrat",sans-serif}
.cta-main{left:110px;top:97px;font:500 29px "Montserrat",sans-serif;text-transform:uppercase;letter-spacing:.5px}
.cta-btn{left:888px;top:67px;width:201px;height:51px;background:var(--teal-dark)}

/* map */
.map{left:0;top:2711px;width:1200px;height:429px;background:linear-gradient(135deg,#cfcfcf,#e4e4e4 45%,#d3d3d3)}

/* footer */
.footer{left:0;top:3140px;width:1200px;height:450px;background:linear-gradient(180deg,#262628,#1e1e20)}
.footer h4{font:700 14px "Lato",sans-serif;text-transform:uppercase;position:absolute}
.field{position:absolute;border:1px solid #cfcfcf;font-size:14px;padding:14px 12px;color:var(--white)}
.send{left:113px;top:272px;width:167px;height:50px}
.contact-row{position:absolute;left:637px;display:flex;align-items:center;gap:20px;font-size:14px;line-height:22px}
.contact-row .ico{width:36px;height:36px;border:1px solid var(--white);border-radius:50%;display:flex;align-items:center;justify-content:center;flex:none}
.contact-row svg{width:16px;height:16px}
.links{left:957px;top:112px;list-style:none;font-size:14px}
.links li{height:34px;display:flex;gap:22px}
.copyright{left:0;top:393px;width:1200px;text-align:center;font-size:14px}
</style>
</head>
<body>

<header class="abs hero">
  <div class="abs hero-left" role="img" aria-label="Photo of a gutted room under renovation with a ladder and debris"></div>
  <div class="abs hero-right" role="img" aria-label="Photo of the finished living room with a mustard sofa and pendant lights"></div>
  <div class="abs brand"><i></i>LARCHFIELD PROPERTY</div>
  <nav class="abs nav">
    <a class="active" href="#">Home</a><a href="#">About Us</a><a href="#">Development</a><a href="#">Interior Design</a><a href="#">Services</a><a href="#">Contact Us</a>
  </nav>
  <div class="abs nav-rule"></div>
  <div class="abs dots"><b></b><b></b><b class="on"></b><b></b><b></b></div>
</header>

<section class="abs about">
  <div class="abs about-bg" role="img" aria-label="Photo looking up at glass office towers"></div>
  <h2 class="abs heading about-title">About <span>Larchfield<br>Property</span></h2>
  <p class="abs about-copy">Lorem ipsum dolor sit amet, consectetur adipiscing elit, sed do eiusmod tempor incididunt ut labore et dolore magna aliqua. Ut enim ad minim veniam, quis nostrud exercitation ullamco laboris nisi ut aliquip ex ea commodo consequat. Duis aute irure dolor in reprehenderit in voluptate velit esse cillum dolore eu fugiat nulla pariatur. Excepteur sint occaecat cupidatat non proident, sunt in culpa.</p>
  <a class="abs pill about-btn">Read More <svg viewBox="0 0 16 16"><circle cx="8" cy="8" r="8" fill="#fff"/><path d="M6.5 4.5 10 8l-3.5 3.5" stroke="#7f9e97" stroke-width="2" fill="none"/></svg></a>
  <div class="abs about-photo" role="img" aria-label="Photo of a bright converted sitting room with a chandelier"></div>
</section>

<section class="abs services" aria-label="Our services">
  <h2 class="abs heading services-title">Our <span>Services</span></h2>
  <p class="abs services-copy">Sed ut perspiciatis unde omnis iste natus error sit voluptatem accusantium doloremque laudantium, totam rem aperiam, eaque ipsa quae ab illo inventore veritatis et quasi architecto beatae vitae dicta sunt explicabo.</p>
  <div class="abs service" style="left:112px"><svg viewBox="0 0 132 132"><rect x="21" y="21" width="90" height="90" rx="6" transform="rotate(45 66 66)" fill="none" stroke="#fff" stroke-width="2"/><g fill="none" stroke="#fff" stroke-width="2"><rect x="48" y="46" width="30" height="38" rx="2"/><path d="M54 56h18M54 64h18M54 72h10M78 50l8-6 4 4-8 6"/></g></svg><p>Lorem Ipsum</p></div>
  <div class="abs service" style="left:275px"><svg viewBox="0 0 132 132"><rect x="21" y="21" width="90" height="90" rx="6" transform="rotate(45 66 66)" fill="none" stroke="#fff" stroke-width="2"/><g fill="none" stroke="#fff" stroke-width="2"><path d="M44 64 66 46l22 18M50 60v24h32V60"/><rect x="60" y="70" width="12" height="14"/></g></svg><p>Lorem Ipsum</p></div>
  <div class="abs service" style="left:438px"><svg viewBox="0 0 132 132"><rect x="21" y="21" width="90" height="90" rx="6" transform="rotate(45 66 66)" fill="none" stroke="#fff" stroke-width="2"/><g fill="none" stroke="#fff" stroke-width="2"><rect x="50" y="44" width="32" height="42"/><path d="M56 52h6M70 52h6M56 60h6M70 60h6M56 68h6M70 68h6M62 86v-8h8v8"/></g></svg><p>Lorem Ipsum</p></div>
  <div class="abs service" style="left:600px"><svg viewBox="0 0 132 132"><rect x="21" y="21" width="90" height="90" rx="6" transform="rotate(45 66 66)" fill="none" stroke="#fff" stroke-width="2"/><g fill="none" stroke="#fff" stroke-width="2"><rect x="58" y="42" width="24" height="32"/><path d="M63 50h5M72 50h5M63 58h5M72 58h5M44 78c8-4 14 4 22 4h18l6-6"/></g></svg><p>Lorem Ipsum</p></div>
  <div class="abs service" style="left:763px"><svg viewBox="0 0 132 132"><rect x="21" y="21" width="90" height="90" rx="6" transform="rotate(45 66 66)" fill="none" stroke="#fff" stroke-width="2"/><g fill="none" stroke="#fff" stroke-width="2"><path d="M44 84V62h44v22M52 62V52h28v10M66 44v8"/><rect x="60" y="72" width="12" height="12"/><path d="M50 70h6M76 70h6"/></g></svg><p>Lorem Ipsum</p></div>
  <div class="abs service" style="left:926px"><svg viewBox="0 0 132 132"><rect x="21" y="21" width="90" height="90" rx="6" transform="rotate(45 66 66)" fill="none" stroke="#fff" stroke-width="2"/><g fill="none" stroke="#fff" stroke-width="2"><rect x="46" y="46" width="40" height="40"/><path d="M52 54h6M63 54h6M74 54h6M52 64h6M63 64h6M74 64h6M60 86v-10h12v10"/></g></svg><p>Lorem Ipsum</p></div>
</section>

<section class="abs projects">
  <h2 class="abs heading projects-title">Recent <span>Projects</span></h2>
  <div class="abs tile" style="left:114px;top:173px;background:linear-gradient(160deg,#eeeeec,#b9bcc2 60%,#4d5565)" role="img" aria-label="Photo of a living room with a dark sofa"></div>
  <div class="abs tile" style="left:360px;top:173px;background:linear-gradient(170deg,#ebe8e2,#d6d1c8 60%,#bdb7ab)" role="img" aria-label="Photo of a bright sitting room with chandelier"></div>
  <div class="abs tile" style="left:605px;top:173px;background:linear-gradient(200deg,#9ec3e8,#3d6fa6 50%,#1e3557)" role="img" aria-label="Photo of glass towers against a blue sky"></div>
  <div class="abs tile" style="left:851px;top:173px;background:linear-gradient(180deg,#a8a9b0,#6e6557 55%,#2f4a52)" role="img" aria-label="Photo of old stone cottages beside a river"></div>
  <div class="abs tile" style="left:114px;top:412px;background:linear-gradient(170deg,#4a463f,#7a6a52 60%,#5b5448)" role="img" aria-label="Photo of an old stone commercial building"></div>
  <div class="abs tile" style="left:360px;top:412px;background:linear-gradient(180deg,#ecebe8,#c6b69c 55%,#3f6a8c)" role="img" aria-label="Photo of a bedroom with a wooden bed"></div>
  <div class="abs tile tile-hover" style="left:605px;top:412px">
    <svg width="16" height="16" viewBox="0 0 16 16" fill="none" stroke="#fff" stroke-width="2"><circle cx="7" cy="7" r="5"/><path d="M11 11l4 4M5 7h4M7 5v4"/></svg>
    <h3>Lorem Ipsum Dolor</h3>
    <p>Sed ut perspiciatis unde omnis iste natus errvoluptatem accusantium dolore.</p>
    <a href="#"><u>Read More</u> <svg width="13" height="13" viewBox="0 0 16 16" fill="none" stroke="#fff" stroke-width="2"><circle cx="8" cy="8" r="7"/><path d="M7 5l3 3-3 3"/></svg></a>
  </div>
  <div class="abs tile" style="left:851px;top:412px;background:linear-gradient(180deg,#d9d9d6,#a08660 50%,#5d6b35)" role="img" aria-label="Photo of a grand country house on a lawn"></div>
</section>

<section class="abs cta">
  <svg class="abs cta-side" viewBox="0 0 1200 188" preserveAspectRatio="none"><path d="M855 0H1200V188H855L795 94Z" fill="#9bb3ad"/></svg>
  <p class="abs cta-lead">Have any ideas in your mind?</p>
  <p class="abs cta-main">Create your next project with us</p>
  <a class="abs pill cta-btn">Request a Quote <svg viewBox="0 0 16 16"><circle cx="8" cy="8" r="8" fill="#fff"/><path d="M6.5 4.5 10 8l-3.5 3.5" stroke="#6f8f88" stroke-width="2" fill="none"/></svg></a>
</section>

<div class="abs map" role="img" aria-label="Greyscale map of the area south west of London"></div>

<footer class="abs footer">
  <h4 style="left:112px;top:80px">Get in Touch</h4>
  <div class="field" style="left:113px;top:117px;width:217px;height:46px">Name</div>
  <div class="field" style="left:340px;top:117px;width:217px;height:46px">Email</div>
  <div class="field" style="left:113px;top:177px;width:444px;height:83px">Message</div>
  <a class="abs pill send">Send Message <svg viewBox="0 0 16 16"><circle cx="8" cy="8" r="8" fill="#fff"/><path d="M6.5 4.5 10 8l-3.5 3.5" stroke="#7f9e97" stroke-width="2" fill="none"/></svg></a>

  <h4 style="left:637px;top:80px">Contact Us</h4>
  <div class="contact-row" style="top:120px"><span class="ico"><svg viewBox="0 0 16 16" fill="none" stroke="#fff" stroke-width="1.6"><path d="M8 15s5-5 5-9A5 5 0 0 0 3 6c0 4 5 9 5 9z"/><circle cx="8" cy="6" r="1.8"/></svg></span><span>196 , Lorem ipsum dolor<br>United Kingdom</span></div>
  <div class="contact-row" style="top:183px"><span class="ico"><svg viewBox="0 0 16 16" fill="none" stroke="#fff" stroke-width="1.6"><rect x="2" y="4" width="12" height="9" rx="1"/><path d="M2 5l6 4 6-4"/></svg></span><span>info@larchfieldproperty</span></div>
  <div class="contact-row" style="top:238px"><span class="ico"><svg viewBox="0 0 16 16" fill="#fff"><path d="M4 2l2.5 3-1.5 1.5c.8 1.8 2.2 3.2 4 4L10.5 9 13.5 11.5 12 14C7 14 2 9 2 4z"/></svg></span><span>01632 960 418</span></div>

  <h4 style="left:957px;top:80px">Quick Links</h4>
  <ul class="abs links">
    <li><span>»</span>Home</li><li><span>»</span>About Us</li><li><span>»</span>Services</li><li><span>»</span>Recent Projects</li><li><span>»</span>Contact Us</li>
  </ul>
  <p class="abs copyright">© 2020 Larchfield Property. All Rights Reserved</p>
</footer>

</body>
</html>
```